UX Design Document Management App Project

UPDATED PROJECT and INCREASED TOTAL COST. Also added a new design guideline document (4QK - Concept - The Lantern 170613.pdf).

We are a small start-up company based in Sydney, Australia. We have the ideas and coding skills to have built a revolutionary document management app that helps knowledge workers deal with information overload.

We are about to launch an alpha version of a document management app on the iPhone. We have created a series of screens but they lack the brilliance that only a talented graphic designer can deliver. So we would like to find a design partner who can make a contribution in two areas:

1. Make specific changes to our screens such as formatting images so they better blend into the background.
2. Examine our overall UX and either suggest changes or propose new design concepts.
3. Create a logo for this product.

We have completed a pretty comprehensive design brief that we attach to this project and also a set of our existing screen designs in a mix of Photoshop and Keynote formats that we can share with you.

Once we have launched are alpha product, we hope that the winner of this project (our future graphic design partner) will work with us on another project that aims to radically improve the UX of our app in time for a full version 1.0 launch later this year.

We'd like to lock-down the alpha UX in 5 to 10 days but if the ideas you have are exciting enough we can extend this time.
Updates

Project now has a SIGNIFICANTLY INCREASED BUDGET (almost doubled) and an expanded scope to deliver a logo for our product. Check out the additional design brief document just uploaded.

Hello Designers,

Just to let you know that we have updated the project and INCREASED THE TOTAL BUDGET. We have also added a new design guideline document (4QK - Concept - The Lantern 170613.pdf) to help inspire you!

The project now has a significantly increased budget (almost doubled) and an expanded scope to also deliver a logo for our Mollant product. Check out the additional design brief document just uploaded.

Thanks for participating!

All the best,

Gareth

Barring any unforeseen circumstances, this design competition will remain open until midnight Pacific Standard Time this Sunday. That means about 10 am Sydney time this Monday, July 1st. Good luck and get your designs in!

Project Deadline Extended
Reason: I agreed to use PST not AEST!

Target Market(s)

individual knowledge workers: professionals, office workers/managers, university students, academics/researchers, etc.

Industry/Entity Type

Graphic Designer

Requirements
Must have
• professional, highly effective UX

```html
<!DOCTYPE html>
<html lang="en">
<head>
<meta charset="utf-8">
<title>Mollant – Document screens</title>
<link rel="stylesheet" href="https://fonts.googleapis.com/css2?family=Quicksand:wght@400;500&display=swap">
<style>
  :root{
    --teal:#13a99b;
    --teal-dark:#0f7f73;
    --teal-soft:#9fcbbd;
    --coral:#e27272;
    --ink:#222;
    --text:#6c6c6c;
    --rule:#d9d9d9;
    --bar:#999a9d;
    --drawer:#e7e7e9;
    --drawer-rule:#cfcfd2;
    --white:#fff;
  }
  *{box-sizing:border-box;margin:0;padding:0}
  html,body{width:1200px;height:609px;overflow:hidden;background:var(--white)}
  body{position:relative;font-family:"Quicksand",sans-serif;color:var(--text)}

  .screen{position:absolute;top:12px;width:386px;height:583px;overflow:hidden;
    background:linear-gradient(#fff 55%,#f1f1f2 100%);}
  .screen--reader{left:12px}
  .screen--list{left:410px}
  .screen--grid{left:802px}

  .app-bar{height:62px;background:var(--teal);position:relative;color:var(--white)}
  .app-bar__title{position:absolute;left:0;right:0;top:13px;text-align:center;font-size:25px;font-weight:400;letter-spacing:.2px}
  .app-bar__back{position:absolute;left:14px;top:10px}
  .app-bar__settings{position:absolute;right:8px;top:9px}

  .doc-head{position:absolute;left:16px;right:12px;top:72px;height:70px;
    border-top:2px solid var(--rule);border-bottom:2px solid var(--rule)}
  .doc-date{position:absolute;left:2px;top:8px;width:52px;height:52px;border-radius:50%;background:var(--coral);color:var(--white);text-align:center}
  .doc-date__day{display:block;font-size:24px;line-height:26px;margin-top:7px}
  .doc-date__month{display:block;font-size:10px;line-height:10px}
  .doc-title{position:absolute;left:72px;top:18px;font-size:18px;color:var(--ink)}
  .doc-subtitle{position:absolute;left:72px;top:41px;font-size:9px;color:#777}

  .doc-body{position:absolute;left:56px;right:56px;top:166px;text-align:center;font-size:16.5px;line-height:23px}
  .doc-body p{margin-bottom:23px}
  .doc-body--muted{filter:blur(4px);opacity:.55}

  .drawer-handle{position:absolute;left:0;right:0;height:20px;background:var(--bar);display:flex;align-items:center;justify-content:center}
  .drawer-handle span{display:block;width:28px;height:9px;background:repeating-linear-gradient(#fff 0 1px,transparent 1px 2.6px)}
  .screen--reader .drawer-handle{bottom:0}
  .screen--list .drawer-handle,.screen--grid .drawer-handle{top:337px}

  .drawer{position:absolute;left:0;right:0;top:357px;bottom:0;background:var(--drawer)}
  .menu{list-style:none;margin:10px 4px 0}
  .menu__item{height:50px;border-top:2px solid var(--drawer-rule);display:flex;align-items:center;font-size:19px;color:#555}
  .menu__item:last-child{border-bottom:2px solid var(--drawer-rule)}
  .menu__dot{width:34px;height:34px;border-radius:50%;background:var(--teal-soft);margin:0 12px 0 16px}

  .tools{position:absolute;left:0;top:0;width:100%;height:100%}
  .tool{position:absolute;width:68px;text-align:center;font-size:11px;line-height:13px;color:#555}
  .tool__tile{width:68px;height:68px;border-radius:3px;background:linear-gradient(#16b3a3,var(--teal-dark));display:flex;align-items:center;justify-content:center;margin-bottom:6px}
</style>
</head>
<body>

<!-- Reader screen -->
<section class="screen screen--reader">
  <header class="app-bar">
    <svg class="app-bar__back" width="40" height="40" viewBox="0 0 40 40"><circle cx="20" cy="20" r="17" fill="none" stroke="#fff" stroke-width="3"/><path d="M29 20H12M19 12l-8 8 8 8" fill="none" stroke="#fff" stroke-width="3.5" stroke-linecap="round" stroke-linejoin="round"/></svg>
    <h1 class="app-bar__title">Mollant</h1>
    <svg class="app-bar__settings" width="42" height="42" viewBox="0 0 42 42"><circle cx="21" cy="21" r="18" fill="none" stroke="#fff" stroke-width="3"/><g fill="#fff"><circle cx="21" cy="21" r="8"/><g id="teeth"><rect x="19" y="8" width="4" height="26" rx="1"/><rect x="19" y="8" width="4" height="26" rx="1" transform="rotate(45 21 21)"/><rect x="19" y="8" width="4" height="26" rx="1" transform="rotate(90 21 21)"/><rect x="19" y="8" width="4" height="26" rx="1" transform="rotate(135 21 21)"/></g></g><circle cx="21" cy="21" r="3.5" fill="var(--teal)"/></svg>
  </header>
  <div class="doc-head">
    <div class="doc-date"><span class="doc-date__day">03</span><span class="doc-date__month">May</span></div>
    <h2 class="doc-title">Document Name</h2>
    <p class="doc-subtitle">Lorem ipsum dolor sit amet and</p>
  </div>
  <article class="doc-body">
    <p>This is a page with random text typed into the text box to help fill out the mock up that is being drawn.</p>
    <p>The font selected for the text should be crisp against the white screen, and preferably grey in colour – but not black.</p>
    <p>And so the text continues, on and on, and some more...</p>
  </article>
  <div class="drawer-handle"><span></span></div>
</section>

<!-- List drawer screen -->
<section class="screen screen--list">
  <header class="app-bar">
    <svg class="app-bar__back" width="40" height="40" viewBox="0 0 40 40"><circle cx="20" cy="20" r="17" fill="none" stroke="#fff" stroke-width="3"/><path d="M29 20H12M19 12l-8 8 8 8" fill="none" stroke="#fff" stroke-width="3.5" stroke-linecap="round" stroke-linejoin="round"/></svg>
    <h1 class="app-bar__title">Mollant</h1>
    <svg class="app-bar__settings" width="42" height="42" viewBox="0 0 42 42"><circle cx="21" cy="21" r="18" fill="none" stroke="#fff" stroke-width="3"/><g fill="#fff"><circle cx="21" cy="21" r="8"/><rect x="19" y="8" width="4" height="26" rx="1"/><rect x="19" y="8" width="4" height="26" rx="1" transform="rotate(45 21 21)"/><rect x="19" y="8" width="4" height="26" rx="1" transform="rotate(90 21 21)"/><rect x="19" y="8" width="4" height="26" rx="1" transform="rotate(135 21 21)"/></g><circle cx="21" cy="21" r="3.5" fill="var(--teal)"/></svg>
  </header>
  <div class="doc-head">
    <div class="doc-date"><span class="doc-date__day">03</span><span class="doc-date__month">May</span></div>
    <h2 class="doc-title">Document Name</h2>
    <p class="doc-subtitle">Lorem ipsum dolor sit amet and</p>
  </div>
  <article class="doc-body doc-body--muted" aria-hidden="true">
    <p>This is a page with random text typed into the text box to help fill out the mock up that is being drawn.</p>
    <p>The font selected for the text should be crisp against the white screen, and preferably grey in colour – but not black.</p>
  </article>
  <div class="drawer-handle"><span></span></div>
  <nav class="drawer">
    <ul class="menu">
      <li class="menu__item"><span class="menu__dot"></span>Infographs</li>
      <li class="menu__item"><span class="menu__dot"></span>Semantic Cloud</li>
      <li class="menu__item"><span class="menu__dot"></span>Word Cloud</li>
      <li class="menu__item"><span class="menu__dot"></span>Options</li>
    </ul>
  </nav>
</section>

<!-- Grid drawer screen -->
<section class="screen screen--grid">
  <header class="app-bar">
    <svg class="app-bar__back" width="40" height="40" viewBox="0 0 40 40"><circle cx="20" cy="20" r="17" fill="none" stroke="#fff" stroke-width="3"/><path d="M29 20H12M19 12l-8 8 8 8" fill="none" stroke="#fff" stroke-width="3.5" stroke-linecap="round" stroke-linejoin="round"/></svg>
    <h1 class="app-bar__title">Mollant</h1>
    <svg class="app-bar__settings" width="42" height="42" viewBox="0 0 42 42"><circle cx="21" cy="21" r="18" fill="none" stroke="#fff" stroke-width="3"/><g fill="#fff"><circle cx="21" cy="21" r="8"/><rect x="19" y="8" width="4" height="26" rx="1"/><rect x="19" y="8" width="4" height="26" rx="1" transform="rotate(45 21 21)"/><rect x="19" y="8" width="4" height="26" rx="1" transform="rotate(90 21 21)"/><rect x="19" y="8" width="4" height="26" rx="1" transform="rotate(135 21 21)"/></g><circle cx="21" cy="21" r="3.5" fill="var(--teal)"/></svg>
  </header>
  <div class="doc-head">
    <div class="doc-date"><span class="doc-date__day">03</span><span class="doc-date__month">May</span></div>
    <h2 class="doc-title">Document Name</h2>
    <p class="doc-subtitle">Lorem ipsum dolor sit amet and</p>
  </div>
  <article class="doc-body doc-body--muted" aria-hidden="true">
    <p>This is a page with random text typed into the text box to help fill out the mock up that is being drawn.</p>
    <p>The font selected for the text should be crisp against the white screen, and preferably grey in colour – but not black.</p>
  </article>
  <div class="drawer-handle"><span></span></div>
  <nav class="drawer">
    <div class="tools">
      <div class="tool" style="left:26px;top:15px">
        <div class="tool__tile"><svg width="36" height="44" viewBox="0 0 36 44"><path d="M2 2h22l10 10v30H2z" fill="#fff"/><path d="M24 2v10h10" fill="#d6efec"/><g fill="var(--teal-dark)"><rect x="8" y="26" width="20" height="3"/><rect x="8" y="32" width="20" height="3"/></g></svg></div>
        Infograph
      </div>
      <div class="tool" style="left:157px;top:15px">
        <div class="tool__tile"><svg width="48" height="30" viewBox="0 0 48 30"><path d="M10 28a9 9 0 0 1 0-18 13 13 0 0 1 25-2 10 10 0 0 1 3 20z" fill="#fff"/></svg></div>
        Semantic<br>Cloud
      </div>
      <div class="tool" style="left:289px;top:15px">
        <div class="tool__tile"><svg width="56" height="40" viewBox="0 0 56 40"><path d="M26 20a8 8 0 0 1 0-16 11 11 0 0 1 21-1 8 8 0 0 1 2 17z" fill="#fff"/><path d="M9 38a8 8 0 0 1 0-16 12 12 0 0 1 23-2 9 9 0 0 1 2 18z" fill="#fff"/></svg></div>
        Word<br>Cloud
      </div>
      <div class="tool" style="left:26px;top:135px">
        <div class="tool__tile"><svg width="40" height="44" viewBox="0 0 40 44"><path d="M26 3l9 6-16 24-9-6z" fill="#fff"/><path d="M10 27l9 6-10 6z" fill="#fff"/></svg></div>
        Sample
      </div>
      <div class="tool" style="left:157px;top:135px">
        <div class="tool__tile"><svg width="40" height="40" viewBox="0 0 40 40"><circle cx="16" cy="16" r="10" fill="none" stroke="#fff" stroke-width="5"/><path d="M24 24l11 11" stroke="#fff" stroke-width="7" stroke-linecap="round"/></svg></div>
        Option
      </div>
      <div class="tool" style="left:289px;top:135px">
        <div class="tool__tile"><svg width="34" height="34" viewBox="0 0 34 34"><path d="M5 5l24 24M29 5L5 29" stroke="#fff" stroke-width="7" stroke-linecap="round"/></svg></div>
        Text
      </div>
    </div>
  </nav>
</section>

</body>
</html>
```